Web Design for a recruitment company

Website is for a recruitment company, with a particular focus on temporary staff, trades, skilled, and unskilled labour markets. Website will consist of a home page design and separate design for additional pages. Website will be implemented as a template in SharePoint. There is a separate design project for a new logo and look colours will need to be co-ordinated.

Target Market(s)

Company executives in the construction and trades areas looking for staff. Trades people, skilled and unskilled labourers looking for work.

Industry/Entity Type

It Company

Number of Pages Required

2 page

Requirements
Must have
• Looking for Home Page design plus design for additional pages.
• .
Nice to have
• Right People | Right Place is the firms byline, company name is Voskin Staffing. They will be in the Logo (separate project) but may also appear elsewhere in the design.
• Company values (attached file) may be reflected in the design where practical.

```html
<!DOCTYPE html>
<html lang="en">
<head>
<meta charset="utf-8">
<title>Voskin Staffing — Right People | Right Place</title>
<link href="https://fonts.googleapis.com/css2?family=Open+Sans:ital,wght@0,400;0,600;0,700;1,400&family=Noto+Serif:wght@400;700&display=swap" rel="stylesheet">
<style>
:root{
  --blue:#0fa3e6;
  --orange:#f0913a;
  --green:#1fb887;
  --ink:#333;
  --line:#dcdcdc;
  --pale:#f2f2f2;
  --footer:#333333;
  --black:#111;
  --white:#fff;
}
*{box-sizing:border-box;margin:0;padding:0}
html,body{width:716px;height:1200px;overflow:hidden}
body{position:relative;background:var(--white);font-family:"Open Sans",Arial,sans-serif;color:var(--ink)}
.abs{position:absolute}

/* hero */
.hero{left:0;top:0;width:716px;height:356px}
.hero-photo{position:absolute;inset:0;background:linear-gradient(100deg,#3e3e40 0%,#6a6b6e 35%,#54565a 60%,#2b2c2e 100%)}
.hero-shade{position:absolute;inset:0;background:rgba(0,0,0,.35)}
.topbar{position:absolute;left:0;top:0;width:716px;height:55px;border-bottom:1px solid rgba(255,255,255,.18)}
.brand{position:absolute;left:96px;top:12px;display:flex;align-items:center;gap:8px;color:var(--white)}
.brand-square{width:18px;height:18px;background:var(--white)}
.brand-name{font-family:"Noto Serif",Georgia,serif;font-weight:700;font-size:19px;line-height:20px}
.brand-tag{font-size:9.5px;line-height:12px}
.nav{position:absolute;left:292px;top:18px;display:flex;gap:2px}
.nav a{font-family:"Noto Serif",Georgia,serif;font-size:8.3px;color:var(--white);text-decoration:none;padding:6px 8px;letter-spacing:.2px}
.nav a.active{background:rgba(30,30,30,.75)}
.login{position:absolute;left:626px;top:14px;width:90px;height:28px;background:var(--blue);color:var(--white);font-size:9.5px;font-weight:600;display:flex;align-items:center;justify-content:center;clip-path:polygon(10px 0,100% 0,100% 100%,10px 100%,0 50%)}
.headline{position:absolute;left:0;top:114px;width:716px;display:flex;justify-content:center;align-items:center;color:var(--white);font-weight:600;font-size:28.5px;letter-spacing:.5px}
.headline .sep{width:1px;height:28px;background:rgba(255,255,255,.5);margin:0 21px}
.lead{position:absolute;left:0;top:160px;width:716px;text-align:center;color:var(--white);font-family:"Noto Serif",Georgia,serif;font-size:13px;line-height:17px}
.search{position:absolute;left:96px;top:214px;width:524px;height:31px;border:1px solid rgba(255,255,255,.4);padding:4px 5px;display:flex;gap:4px}
.field{height:21px;background:var(--white);font-size:7.5px;font-style:italic;color:#888;display:flex;align-items:center;padding:0 9px;position:relative}
.field.select::after{content:"";position:absolute;right:7px;top:6px;border:3px solid transparent;border-bottom-color:#555;border-top:none}
.field.select::before{content:"";position:absolute;right:7px;top:11px;border:3px solid transparent;border-top-color:#555;border-bottom:none}
.btn-search{width:86px;height:21px;background:var(--blue);color:var(--white);font-size:8px;font-weight:700;display:flex;align-items:center;justify-content:center}

/* partners */
.partners{left:0;top:356px;width:716px;height:52px;border-bottom:1px solid var(--line);display:flex;justify-content:center;align-items:center;gap:18px;font-size:11px;font-weight:600;color:#a9a9a9}

/* jobs */
.section-title{font-family:"Noto Serif",Georgia,serif;font-weight:400;color:var(--blue);font-size:17px;white-space:nowrap}
.jobs-title{left:95px;top:432px;width:349px;text-align:center}
.jobs{left:95px;top:466px;width:349px;height:178px;border:1px solid var(--line);border-radius:2px}
.job{height:35.2px;display:flex;align-items:center;border-bottom:1px solid var(--line)}
.job:last-child{border-bottom:none}
.job-logo{width:17px;height:17px;background:#e6e6e6;border:1px solid #ccc;margin:0 9px 0 14px}
.job-info{width:132px;border-right:1px solid var(--line);height:100%;display:flex;flex-direction:column;justify-content:center}
.job-role{font-size:8.5px;font-weight:600;color:#444;line-height:10px}
.job-dept{font-size:6.5px;color:#888;line-height:9px}
.job-place{width:120px;border-right:1px solid var(--line);height:100%;display:flex;align-items:center;padding-left:18px;font-size:7.3px;color:#444;gap:6px}
.job-type{margin-left:11px;width:57px;height:15px;color:var(--white);font-size:6.8px;font-weight:600;display:flex;align-items:center;justify-content:center}
.full{background:var(--blue)}.part{background:var(--orange)}.free{background:var(--green)}
.load-more{left:95px;top:650px;width:349px;height:20px;background:var(--blue);border-radius:2px;color:var(--white);font-size:8px;font-weight:700;display:flex;align-items:center;justify-content:center}

/* call back */
.callback{left:458px;top:438px;width:162px;height:206px;border:1px solid var(--line);border-radius:2px;padding:0 13px}
.callback-head{display:flex;align-items:center;gap:7px;height:31px;margin-top:8px;border-bottom:1px solid var(--line)}
.callback-head .section-title{font-size:11px}
.callback-note{font-size:6.5px;color:#666;line-height:8.5px;margin:10px 0 5px}
.input{height:18px;background:#ededed;font-size:6.6px;font-style:italic;color:#888;display:flex;align-items:center;padding:0 9px;margin-top:6px;position:relative}
.input.select::after{content:"";position:absolute;right:7px;top:8px;border:3px solid transparent;border-top-color:#999;border-bottom:none}
.btn-call{height:22px;background:var(--blue);color:var(--white);font-size:8px;font-weight:600;display:flex;align-items:center;justify-content:center;margin-top:7px}

/* stats */
.stats{left:0;top:702px;width:716px;height:199px;background:var(--pale)}
.stats-map{position:absolute;left:100px;top:0;width:520px;height:150px;background:radial-gradient(ellipse at center,#e9e9e9 0%,rgba(242,242,242,0) 70%)}
.stats-title{position:absolute;top:30px;width:716px;text-align:center}
.stats-text{position:absolute;top:58px;width:716px;text-align:center;font-size:8.8px;line-height:12px;color:#555}
.stat-row{position:absolute;left:127px;top:110px;width:462px;height:51px;display:flex}
.stat{flex:1;text-align:center;border-right:1px solid #d8d8d8}
.stat:last-child{border-right:none}
.stat-num{font-size:20px;color:#555;line-height:28px}
.stat-label{font-size:8.6px;color:#777;line-height:11px}

/* register */
.register{left:0;top:901px;width:716px;height:147px;background:var(--blue);color:var(--white);text-align:center}
.register h2{font-family:"Noto Serif",Georgia,serif;font-weight:400;font-size:16px;margin-top:28px}
.register p{font-size:8.6px;line-height:12px;margin-top:10px}
.btn-register{position:absolute;left:310px;top:93px;width:96px;height:20px;background:var(--white);color:#444;font-size:7.5px;font-weight:600;display:flex;align-items:center;justify-content:center}

/* footer */
.footer{left:0;top:1048px;width:716px;height:106px;background:var(--footer);color:var(--white)}
.footer-cols{position:absolute;left:96px;top:27px;width:524px;display:flex;gap:11px}
.footer-col{flex:1;text-align:center}
.footer-col h3{font-family:"Noto Serif",Georgia,serif;font-weight:400;font-size:9.5px;padding-bottom:8px;border-bottom:2px solid #2a2a2a}
.footer-col p{font-size:7.5px;line-height:10px;margin-top:8px}
.bottom{left:0;top:1154px;width:716px;height:46px;background:var(--black)}
</style>
</head>
<body>

<header class="abs hero">
  <div class="hero-photo" role="img" aria-label="Blurred office photo of a person typing at a keyboard beside a coffee press"></div>
  <div class="hero-shade"></div>
  <div class="topbar">
    <div class="brand">
      <div class="brand-square"></div>
      <div>
        <div class="brand-name">Voskin Staffing</div>
        <div class="brand-tag">Right People &nbsp;|&nbsp; Right Place</div>
      </div>
    </div>
    <nav class="nav">
      <a class="active">HOME</a><a>ABOUT US</a><a>JOBS</a><a>CANDIDATES</a><a>CONTACT US</a><a>BLOG</a>
    </nav>
    <div class="login">LOGIN</div>
  </div>
  <h1 class="headline">RIGHT PEOPLE<span class="sep"></span>RIGHT PLACE</h1>
  <p class="lead">This is Studio's version &nbsp;of Lorem Ipsum. Proin gravida nibh vel velit auctor aliquet.<br>Aenean sollicitudin, lorem quis bibendum auctor,</p>
  <form class="search">
    <div class="field" style="width:158px">Keywords</div>
    <div class="field select" style="width:129px">All Regions</div>
    <div class="field select" style="width:129px">Any Category</div>
    <div class="btn-search">SEARCH</div>
  </form>
  <svg class="abs" style="left:350px;top:287px" width="16" height="28" viewBox="0 0 16 28">
    <rect x="2" y="1" width="12" height="20" rx="6" fill="none" stroke="#fff" stroke-width="1.3"/>
    <line x1="8" y1="5" x2="8" y2="9" stroke="#fff" stroke-width="1.3"/>
    <line x1="8" y1="21" x2="8" y2="26" stroke="#fff" stroke-width="1"/>
    <path d="M6 24 L8 27 L10 24" fill="#fff"/>
  </svg>
</header>

<section class="abs partners" aria-label="Partner companies">
  <span>Northvale</span><span>Quillpay</span><span>Fizzora</span><span>Ledgerly</span><span>Tradeloop</span><span>Starglen</span><span>Corvane</span><span>Bramwick</span><span>Orbelle</span>
</section>

<h2 class="abs section-title jobs-title">Our Latest Jobs</h2>
<section class="abs jobs">
  <div class="job"><div class="job-logo"></div><div class="job-info"><div class="job-role">Senior Graphic Designer</div><div class="job-dept">Design Technology</div></div><div class="job-place"><svg width="7" height="9" viewBox="0 0 7 9"><path d="M3.5 .6a2.9 2.9 0 0 0-2.9 2.9C.6 5.6 3.5 8.4 3.5 8.4S6.4 5.6 6.4 3.5A2.9 2.9 0 0 0 3.5.6z" fill="none" stroke="#444" stroke-width="1.1"/><circle cx="3.5" cy="3.4" r="1" fill="#444"/></svg>New York</div><div class="job-type full">Full-Time</div></div>
  <div class="job"><div class="job-logo"></div><div class="job-info"><div class="job-role">Duty Manager</div><div class="job-dept">Restaurant Customer Host</div></div><div class="job-place"><svg width="7" height="9" viewBox="0 0 7 9"><path d="M3.5 .6a2.9 2.9 0 0 0-2.9 2.9C.6 5.6 3.5 8.4 3.5 8.4S6.4 5.6 6.4 3.5A2.9 2.9 0 0 0 3.5.6z" fill="none" stroke="#444" stroke-width="1.1"/><circle cx="3.5" cy="3.4" r="1" fill="#444"/></svg>San Francisco</div><div class="job-type part">Part-Time</div></div>
  <div class="job"><div class="job-logo"></div><div class="job-info"><div class="job-role">Web Developer</div><div class="job-dept">Design Technology</div></div><div class="job-place"><svg width="7" height="9" viewBox="0 0 7 9"><path d="M3.5 .6a2.9 2.9 0 0 0-2.9 2.9C.6 5.6 3.5 8.4 3.5 8.4S6.4 5.6 6.4 3.5A2.9 2.9 0 0 0 3.5.6z" fill="none" stroke="#444" stroke-width="1.1"/><circle cx="3.5" cy="3.4" r="1" fill="#444"/></svg>New York</div><div class="job-type full">Full-Time</div></div>
  <div class="job"><div class="job-logo"></div><div class="job-info"><div class="job-role">Web Developer</div><div class="job-dept">Design Technology</div></div><div class="job-place"><svg width="7" height="9" viewBox="0 0 7 9"><path d="M3.5 .6a2.9 2.9 0 0 0-2.9 2.9C.6 5.6 3.5 8.4 3.5 8.4S6.4 5.6 6.4 3.5A2.9 2.9 0 0 0 3.5.6z" fill="none" stroke="#444" stroke-width="1.1"/><circle cx="3.5" cy="3.4" r="1" fill="#444"/></svg>London</div><div class="job-type full">Full-Time</div></div>
  <div class="job"><div class="job-logo"></div><div class="job-info"><div class="job-role">Senior Graphic Designer</div><div class="job-dept">Design Technology</div></div><div class="job-place"><svg width="7" height="9" viewBox="0 0 7 9"><path d="M3.5 .6a2.9 2.9 0 0 0-2.9 2.9C.6 5.6 3.5 8.4 3.5 8.4S6.4 5.6 6.4 3.5A2.9 2.9 0 0 0 3.5.6z" fill="none" stroke="#444" stroke-width="1.1"/><circle cx="3.5" cy="3.4" r="1" fill="#444"/></svg>Miami</div><div class="job-type free">Freelance</div></div>
</section>
<div class="abs load-more">+ LOAD MORE LISTINGS</div>

<aside class="abs callback">
  <div class="callback-head">
    <svg width="18" height="17" viewBox="0 0 20 18"><path d="M3 10V8a7 7 0 0 1 14 0v2" fill="none" stroke="#444" stroke-width="1.4"/><rect x="1.5" y="9" width="3.5" height="5" rx="1.2" fill="#444"/><rect x="15" y="9" width="3.5" height="5" rx="1.2" fill="#444"/><path d="M16.5 14c0 2-2 3-5 3" fill="none" stroke="#444" stroke-width="1"/><circle cx="10" cy="9" r="3.3" fill="none" stroke="#444" stroke-width="1"/></svg>
    <h2 class="section-title">Request a Call Back</h2>
  </div>
  <p class="callback-note">This is Studio's version &nbsp;of Lorem Ipsum. Proin gravida nibh vel velit</p>
  <div class="input">Name</div>
  <div class="input">Email</div>
  <div class="input">Phone Number</div>
  <div class="input select">I'm a...... please select</div>
  <div class="btn-call">Call Me Back</div>
</aside>

<section class="abs stats">
  <div class="stats-map" role="img" aria-label="Faint world map backdrop"></div>
  <h2 class="section-title stats-title">Voskin Staffing Site Stats</h2>
  <p class="stats-text">Here we list our site stats and how many people we've helped find a job and companies have found recruits.<br>It's a pretty awesome stats area!</p>
  <div class="stat-row">
    <div class="stat"><div class="stat-num">44</div><div class="stat-label">Jobs Posted</div></div>
    <div class="stat"><div class="stat-num">50</div><div class="stat-label">Resumes Posted</div></div>
    <div class="stat"><div class="stat-num">104</div><div class="stat-label">Jobs Filled</div></div>
    <div class="stat"><div class="stat-num">91</div><div class="stat-label">Companies</div></div>
    <div class="stat"><div class="stat-num">2,152</div><div class="stat-label">Members</div></div>
  </div>
</section>

<section class="abs register">
  <h2>Register as a Candidate Now !</h2>
  <p>This is Studio's version &nbsp;of Lorem Ipsum. Proin gravida nibh vel velit auctor aliquet. Aenean sollicitudin, lorem quis bibendum<br>auctor, nisi elit consequat ipsum, nec sagittis sem nibh id elit.</p>
  <div class="btn-register">REGISTER NOW</div>
</section>

<footer class="abs footer">
  <div class="footer-cols">
    <div class="footer-col"><h3>Call</h3><p>1800-555-210</p></div>
    <div class="footer-col"><h3>Email</h3><p>hello@voskinstaffing.com</p></div>
    <div class="footer-col"><h3>Follow</h3><p>Linkora | Chirpit | RSS</p></div>
    <div class="footer-col"><h3>Visit</h3><p>42 Harbour Lane, Unit 7,<br>Lorem Ipsum Vestibulum 210/04</p></div>
  </div>
</footer>
<div class="abs bottom"></div>

</body>
</html>
```